Flyer-Design für Vertrieb von LED-Beleuchtung
Zielgruppe
Vertrieb von Led Beleuchtung,, für Biergärten
Shop-Adresse lautet www.brilo-nox-markt.de diese sollte auch unbedingt mit rein!
Aufgabenstellung
Es geht Hauptsächlich nur um Bunte Led Birnen und die dazugehörigen Fassungen.
Daher bitte eigene Bilder benutzen und zusätzlich noch welche suchen die passen würden.
Aussagen soll es wie sehr man durch die Umstellung auf unsere Birnen sparen kann und dass sie besser Leuchten als normale und nicht kaputt gehen. 2 alte Flyerversuche von mir selbst liegen bei zwecks preise etc. Die Antwortkarte darf nicht mehr drauf sein da dies bereits Formatprobleme mit der Post gab

```html
<!DOCTYPE html>
<html lang="de">
<head>
<meta charset="utf-8">
<title>LUMO-VEX – Stromsparende LED Beleuchtung</title>
<link href="https://fonts.googleapis.com/css2?family=Open+Sans:wght@400;600;700&display=swap" rel="stylesheet">
<style>
  :root {
    --ink-black: #000000;
    --paper-white: #ffffff;
    --text-dark: #1a1a1a;
    --text-light: #ffffff;
    --accent-yellow: #f5e600;
    --night-blue: #05070d;
    --velvet-brown: #6b3512;
    --velvet-gold: #a2622a;
  }
  * { margin: 0; padding: 0; box-sizing: border-box; }
  html, body { width: 1200px; height: 848px; overflow: hidden; background: var(--ink-black); }
  body { font-family: "Open Sans", sans-serif; }
  .flyer { position: relative; width: 1200px; height: 848px; background: var(--ink-black); overflow: hidden; }
  .hero-photo {
    position: absolute; left: 398px; top: 202px; width: 802px; height: 646px;
    background:
      radial-gradient(ellipse 60% 30% at 60% 55%, rgba(120,160,60,0.18), transparent 70%),
      linear-gradient(180deg, var(--night-blue) 0%, #080a12 58%, #2a160a 66%, var(--velvet-gold) 72%, var(--velvet-brown) 85%, #3a1a08 100%);
  }
  .benefits-panel { position: absolute; left: 0; top: 202px; width: 398px; height: 646px; background: var(--paper-white); }
  .brand { position: absolute; left: 0; width: 1200px; top: 82px; text-align: center; color: var(--text-light); font-weight: 700; font-size: 43px; letter-spacing: 0.5px; }
  .tagline { position: absolute; left: 0; width: 1200px; top: 143px; text-align: center; color: var(--text-light); font-size: 17px; }
  .benefits-title { position: absolute; left: 58px; top: 154px; color: var(--text-light); font-size: 26px; }
  .benefit { position: absolute; left: 52px; width: 340px; color: var(--text-dark); font-size: 17px; line-height: 20.5px; white-space: nowrap; }
  .benefit strong { font-weight: 700; }
  .shop-address { position: absolute; left: 50px; top: 800px; color: var(--text-dark); font-size: 17px; font-weight: 700; }
  .headline { position: absolute; left: 398px; width: 400px; top: 276px; text-align: center; color: var(--accent-yellow); font-size: 26.7px; line-height: 32px; }
  .more-products { position: absolute; left: 830px; top: 165px; width: 360px; color: var(--text-light); font-size: 17px; line-height: 20.5px; white-space: nowrap; }
  .more-products h2 { font-size: 17px; font-weight: 700; line-height: 20.5px; }
  .more-products p + p { margin-top: 20.5px; }
  .sale-price { display: inline-block; margin-top: 6px; color: var(--accent-yellow); font-size: 22px; font-weight: 700; line-height: 26px; }
</style>
</head>
<body>
<div class="flyer">
  <div class="hero-photo" role="img" aria-label="Drei bunte Glühbirnen in Rot, Grün und Orange auf einem Tisch mit braunem Samttuch vor dunklem Hintergrund"></div>
  <div class="benefits-panel"></div>

  <div class="brand">LUMO-VEX</div>
  <div class="tagline">Stromsparende LED Beleuchtung</div>
  <div class="benefits-title">Ihre Vorteile</div>

  <p class="benefit" style="top:238px">1 Jahr Garantie auf alle Leuchtmittel</p>
  <p class="benefit" style="top:279px">Moderne Special Effekts für<br>Standart Fassungen</p>
  <p class="benefit" style="top:341px">Umweltschonend durch niedriegen<br>Stromverbrauch von nur 1 Watt<br>und sehr lange Lebensdauer</p>
  <p class="benefit" style="top:423px">Robustes und stoßfestes Material</p>
  <p class="benefit" style="top:458px">Sparen Sie nicht an Personal oder<br>Qualität, sondern an kostspieliger<br>Außenbeleuchtung.</p>
  <p class="benefit" style="top:554px;left:50px">Jetzt umstellen und Ihre Vorteile ab<br>heute schon nutzen z.B.:</p>
  <p class="benefit" style="top:616px;left:50px"><strong>Statt einer Stromrechnung von<br>4.000EUR</strong></p>
  <p class="benefit" style="top:677px;left:50px">Profitieren Sie durch einfaches<br>Austauschen Ihrer Birnen auf<br>unsere 1 Watt LED- Birnen von<br>einer <strong>Einsparung von bis zu<br>3.898EUR</strong></p>

  <p class="shop-address">www.brilo-nox-markt.de</p>

  <p class="headline">Besser Leuchtkraft als alle<br>Standart Glühbirnen!</p>

  <div class="more-products">
    <h2>Weitere Produkte</h2>
    <p>Gerne beraten wir Sie über individuelle<br>Möglichkeiten Ihren Biergarten<br>auszuleuchten um neue Akzente&nbsp; zu<br>setzen. Fordern Sie noch heute ihr<br>Angebot in unserem Shop an und<br>profitieren Sie schon in kurzer Zeit von<br>Ihren Einsparungen.</p>
    <p>1 Watt LED Birne in den Farben:<br>Weiß, Gelb, Blau, Grün, Gelb, Pink,<br>Zum Sommersale-Preis von nur<br><span class="sale-price">2,99 EUR</span></p>
  </div>
</div>
</body>
</html>
```